Graphic Design for a 3 Banner Tradeshow Setup

We are a Pipe Restoration company that specializes in trenchless pipelining. We need a design for a 3 banner setup to use at tradeshows. See attached "banner specs" for sizing - note the 48" x 92" will be in between the two 36" x 92" banners. See attached "Mock-Up" of information each banner needs and utilize the color scheme of the banners we already have in the "both MLD banners" AI file attached. The final designs should communicate what we do and attract people into our booth. We would like to have graphics of realistic pipes for a before (dirty pipe), after cleaning pipe, and lined pipe - see example of "pipe pictures" attached. I'm not sure if this is something you can generate or if we will need to find images of our own to send. Also, see attached "screenshot-process" to see similar images we would like to use to showcase the process.
Target Market(s)
Homeowners, Property Managers, HOA Communities, Healthcare Facilities & Hospitals, and commercial properties
Industry/Entity Type
Trenchless Pipelining
Look and feel
Each slider illustrates characteristics of the customer's brand and the style your logo design should communicate.

```html
<!DOCTYPE html>
<html lang="en">
<head>
<meta charset="utf-8">
<title>MLD Tradeshow Banners</title>
<link href="https://fonts.googleapis.com/css2?family=Bebas+Neue&family=Montserrat:wght@800&family=Orbitron:wght@900&family=Oswald:wght@600;700&family=Poppins:wght@700&family=Roboto:wght@400&display=swap" rel="stylesheet">
<style>
:root{
  --stage:#e4e2e3;
  --white:#ffffff;
  --blue-top:#2298d4;
  --blue-mid:#1f5fb5;
  --blue-deep:#1c2687;
  --accent:#4cc4f2;
  --cyan:#27b4ef;
  --ink:#1e1e22;
  --navy:#1a4a94;
  --button:#1e8fd6;
  --divider:rgba(60,190,240,.7);
  --photo:#8c96a3;
  --pipes:#8a7a70;
}
*{margin:0;padding:0;box-sizing:border-box}
html,body{width:1200px;height:954px;overflow:hidden;background:var(--stage)}
.stage{position:relative;width:1200px;height:954px}
.banner{position:absolute;top:103px;height:690px;background:var(--white);box-shadow:0 6px 14px rgba(0,0,0,.22);overflow:hidden}
.banner--left{left:70px;width:270px}
.banner--center{left:407px;width:367px}
.banner--right{left:857px;width:270px}
.blue-field{position:absolute;left:0;width:100%;background:linear-gradient(180deg,var(--blue-top) 0%,var(--blue-mid) 45%,var(--blue-deep) 100%)}
.logo-tab{position:absolute;left:0;top:0}
.brand{position:absolute;display:flex;align-items:center;gap:5px;color:var(--ink);font-family:"Oswald",sans-serif;font-weight:700;line-height:1}
.brand-mark{background:var(--blue-mid);display:block}
.brand-sub{position:absolute;font-family:"Oswald",sans-serif;font-weight:700;color:var(--ink);letter-spacing:1.6px;line-height:1}
.c{position:absolute;transform:translateY(-50%);white-space:nowrap;line-height:1}
.headline{font-family:"Orbitron",sans-serif;font-weight:900;color:var(--white);text-align:center;left:0;width:100%;letter-spacing:2px}
.item{font-family:"Bebas Neue",sans-serif;color:var(--white);font-size:23px}
.fix-item{font-family:"Poppins",sans-serif;font-weight:700;color:var(--white);font-size:16.5px;line-height:1.1}
.divider{position:absolute;height:1px;background:var(--divider)}
.icon{position:absolute;transform:translateY(-50%)}
.photo{position:absolute;background:var(--photo)}
.contact{font-family:"Montserrat",sans-serif;font-weight:800;color:var(--navy);text-align:center;left:0;width:100%}
.phone{position:absolute;left:0;width:100%;display:flex;justify-content:center;align-items:center;gap:6px;transform:translateY(-50%);font-family:"Oswald",sans-serif;font-weight:700;color:var(--ink);line-height:1;letter-spacing:-.5px}
.web{position:absolute;background:var(--button);color:var(--white);font-family:"Oswald",sans-serif;font-weight:600;display:flex;align-items:center;justify-content:center;border-radius:2px}
.tagline-pill{position:absolute;background:#2a2f3a;border-radius:6px;display:flex;align-items:center;justify-content:center;font-family:"Bebas Neue",sans-serif;color:var(--cyan)}
.subline{font-family:"Roboto",sans-serif;color:var(--white);text-align:center;left:0;width:100%;font-size:21px}
.base-bar{position:absolute;background:#0d0d10}
</style>
</head>
<body>
<div class="stage">

  <!-- Assess banner -->
  <section class="banner banner--left">
    <div class="blue-field" style="top:5px;height:462px"></div>
    <svg class="logo-tab" width="270" height="72" viewBox="0 0 270 72"><path d="M0 0H175L168 62Q166 71 156 71H0Z" fill="#fff"/></svg>
    <div class="brand" style="left:26px;top:28px;font-size:27px"><span class="brand-mark" style="width:18px;height:18px"></span>MLD</div>
    <div class="brand-sub" style="left:26px;top:55px;font-size:6px">MAIN LINE DRAINWORKS</div>

    <div class="c headline" style="top:110px;font-size:38px">WE</div>
    <div class="c headline" style="top:148px;font-size:38px">ASSESS</div>

    <svg class="icon" style="left:20px;top:205px" width="38" height="36" viewBox="0 0 38 36" fill="var(--accent)"><rect x="6" y="6" width="26" height="13" rx="3" transform="rotate(-12 19 12)"/><circle cx="30" cy="10" r="4" fill="#1f5fb5"/><rect x="8" y="20" width="3" height="12"/><rect x="2" y="30" width="10" height="5"/></svg>
    <div class="c item" style="left:65px;top:206px">CCTV PIPE INVESTIGATION</div>
    <div class="divider" style="left:20px;width:227px;top:237px"></div>

    <svg class="icon" style="left:20px;top:273px" width="38" height="38" viewBox="0 0 38 38"><circle cx="20" cy="19" r="16" fill="var(--accent)"/><path d="M20 19V3A16 16 0 0 1 36 19Z" fill="#1f5fb5"/><path d="M22 17V5A14 14 0 0 1 34 17Z" fill="var(--accent)"/><circle cx="9" cy="19" r="6" fill="#1f5fb5" stroke="var(--accent)" stroke-width="1.5"/></svg>
    <div class="c item" style="left:65px;top:274px">BUDGETARY EVALUATION</div>
    <div class="divider" style="left:20px;width:227px;top:312px"></div>

    <svg class="icon" style="left:20px;top:347px" width="36" height="36" viewBox="0 0 36 36" fill="var(--accent)"><rect x="2" y="2" width="16" height="22" rx="2"/><rect x="5" y="7" width="10" height="2" fill="#1f5fb5"/><rect x="5" y="12" width="10" height="2" fill="#1f5fb5"/><rect x="5" y="17" width="10" height="2" fill="#1f5fb5"/><circle cx="17" cy="28" r="6"/><circle cx="29" cy="28" r="6"/></svg>
    <div class="c item" style="left:65px;top:348px">SCOPE DEVELOPMENT</div>
    <div class="divider" style="left:20px;width:227px;top:388px"></div>

    <svg class="icon" style="left:20px;top:428px" width="36" height="36" viewBox="0 0 36 36" fill="none" stroke="var(--accent)" stroke-width="2.5"><circle cx="22" cy="15" r="9"/><circle cx="22" cy="15" r="3.5"/><path d="M12 22Q8 28 13 33H17"/><path d="M3 10H7M3 18H6M5 4L8 7"/></svg>
    <div class="c item" style="left:65px;top:429px">PROJECT OVERSIGHT</div>

    <div class="photo" role="img" aria-label="Row of four pipe sections: corroded dirty pipe, cleaned pipe and newly lined pipes" style="left:7px;top:470px;width:248px;height:64px;background:var(--pipes)"></div>

    <div class="c contact" style="top:571px;font-size:16px">CONTACT US TODAY!</div>
    <div class="phone" style="top:602px;font-size:30px">
      <svg width="22" height="22" viewBox="0 0 24 24"><circle cx="12" cy="12" r="11" fill="var(--navy)"/><path d="M8 6l2 3-1.5 1.5a8 8 0 0 0 5 5L15 14l3 2-1 2.5C11 19 5 13 5.5 7Z" fill="#fff"/></svg>1-800-555-0142
    </div>
    <div class="web" style="left:22px;top:628px;width:226px;height:23px;font-size:14px">www.mainlinedrainworks.com</div>
  </section>

  <!-- Center banner -->
  <section class="banner banner--center">
    <div class="blue-field" style="top:11px;height:414px"></div>
    <svg class="logo-tab" width="367" height="88" viewBox="0 0 367 88"><path d="M0 0H224L215 76Q213 87 202 87H0Z" fill="#fff"/></svg>
    <div class="brand" style="left:40px;top:35px;font-size:33px"><span class="brand-mark" style="width:24px;height:24px"></span>MLD</div>
    <div class="brand-sub" style="left:40px;top:67px;font-size:7px">MAIN LINE DRAINWORKS</div>

    <div class="c headline" style="top:136px;font-size:48px">PIPE</div>
    <div class="c headline" style="top:174px;font-size:35px;letter-spacing:1px">PROBLEMS?</div>
    <div class="tagline-pill" style="left:40px;top:195px;width:288px;height:32px;font-size:28px">WE HELP FIX PIPE PROBLEMS</div>
    <div class="c subline" style="top:247px">WITHOUT HAVING</div>
    <div class="c subline" style="top:276px">TO TEAR UP YOUR</div>
    <div class="c subline" style="top:304px">BUIDLING</div>

    <div class="photo" role="img" aria-label="High-rise condominium with palm trees and a company service truck" style="left:0;top:344px;width:92px;height:150px"></div>
    <div class="photo" role="img" aria-label="Technician viewing a pipe camera monitor on site" style="left:101px;top:336px;width:149px;height:179px;border-radius:3px"></div>
    <div class="photo" role="img" aria-label="Crew members working at an open drain on a rooftop" style="left:259px;top:344px;width:108px;height:157px"></div>

    <div class="c contact" style="top:542px;font-size:22px">CONTACT US TODAY!</div>
    <div class="phone" style="top:584px;font-size:40px">
      <svg width="30" height="30" viewBox="0 0 24 24"><circle cx="12" cy="12" r="11" fill="var(--navy)"/><path d="M8 6l2 3-1.5 1.5a8 8 0 0 0 5 5L15 14l3 2-1 2.5C11 19 5 13 5.5 7Z" fill="#fff"/></svg>1-800-555-0142
    </div>
    <div class="web" style="left:37px;top:617px;width:289px;height:29px;font-size:19px">www.mainlinedrainworks.com</div>
  </section>

  <!-- Fix banner -->
  <section class="banner banner--right">
    <div class="blue-field" style="top:5px;height:546px"></div>
    <svg class="logo-tab" width="270" height="72" viewBox="0 0 270 72"><path d="M0 0H175L168 62Q166 71 156 71H0Z" fill="#fff"/></svg>
    <div class="brand" style="left:26px;top:28px;font-size:27px"><span class="brand-mark" style="width:18px;height:18px"></span>MLD</div>
    <div class="brand-sub" style="left:26px;top:55px;font-size:6px">MAIN LINE DRAINWORKS</div>

    <div class="c headline" style="top:124px;font-size:44px">WE FIX</div>

    <svg class="icon" style="left:22px;top:181px" width="40" height="38" viewBox="0 0 40 38" fill="var(--accent)"><rect x="2" y="2" width="6" height="16"/><rect x="10" y="4" width="6" height="14"/><path d="M16 10h8a10 10 0 0 1 10 10v2h-8a6 6 0 0 0-6-6h-4Z"/><path d="M2 28q5-4 10 0t10 0 10 0 8 0v8H2Z"/></svg>
    <div class="c fix-item" style="left:77px;top:181px">Slow Drains</div>
    <div class="divider" style="left:22px;width:225px;top:214px"></div>

    <svg class="icon" style="left:22px;top:243px" width="40" height="40" viewBox="0 0 40 40" fill="var(--accent)"><rect x="4" y="2" width="8" height="10"/><rect x="6" y="12" width="4" height="26"/><rect x="22" y="2" width="12" height="36" rx="2"/><circle cx="28" cy="20" r="4" fill="#1f5fb5"/></svg>
    <div class="c fix-item" style="left:77px;top:243px">Back-Ups</div>
    <div class="divider" style="left:22px;width:225px;top:276px"></div>

    <svg class="icon" style="left:22px;top:304px" width="40" height="40" viewBox="0 0 40 40" fill="var(--accent)"><path d="M4 18a16 16 0 0 1 32 0h-5a11 11 0 0 0-22 0Z"/><rect x="15" y="18" width="10" height="16"/><rect x="2" y="34" width="36" height="4"/></svg>
    <div class="c fix-item" style="left:77px;top:304px">Sewer Odors</div>
    <div class="divider" style="left:22px;width:225px;top:336px"></div>

    <svg class="icon" style="left:22px;top:363px" width="40" height="40" viewBox="0 0 40 40" fill="var(--accent)"><rect x="2" y="20" width="14" height="12" rx="2"/><rect x="16" y="8" width="12" height="24" rx="3"/><rect x="18" y="2" width="8" height="6"/><path d="M28 28l4 4M30 24h6M28 36l-2 3" stroke="var(--accent)" stroke-width="2"/></svg>
    <div class="c fix-item" style="left:77px;top:363px">Cracked Pipes</div>
    <div class="divider" style="left:22px;width:225px;top:396px"></div>

    <svg class="icon" style="left:22px;top:423px" width="40" height="40" viewBox="0 0 40 40" fill="none" stroke="var(--accent)" stroke-width="3"><circle cx="22" cy="17" r="11"/><path d="M14 25L4 36"/><path d="M17 20l4-5 4 3 3-5" stroke-width="2"/></svg>
    <div class="c fix-item" style="left:77px;top:423px">Root Intrusion</div>
    <div class="divider" style="left:22px;width:225px;top:456px"></div>

    <svg class="icon" style="left:22px;top:492px" width="40" height="40" viewBox="0 0 40 40" fill="var(--accent)"><path d="M4 6h22v8H14v6H4Z"/><rect x="26" y="4" width="4" height="12"/><circle cx="9" cy="28" r="3"/><path d="M20 22l14 14-3 3-14-14Z"/></svg>
    <div class="c fix-item" style="left:76px;top:493px">Recurring Plumbing<br>Problems</div>

    <div class="base-bar" style="left:25px;top:551px;width:221px;height:14px;clip-path:polygon(0 0,100% 0,97% 100%,3% 100%)"></div>

    <div class="c contact" style="top:586px;font-size:16px">CONTACT US TODAY!</div>
    <div class="phone" style="top:618px;font-size:30px">
      <svg width="22" height="22" viewBox="0 0 24 24"><circle cx="12" cy="12" r="11" fill="var(--navy)"/><path d="M8 6l2 3-1.5 1.5a8 8 0 0 0 5 5L15 14l3 2-1 2.5C11 19 5 13 5.5 7Z" fill="#fff"/></svg>1-800-555-0142
    </div>
    <div class="web" style="left:23px;top:646px;width:225px;height:23px;font-size:14px">www.mainlinedrainworks.com</div>
  </section>

</div>
</body>
</html>
```